Brimwell is a steel frame construction company that builds residential and commercial homes

1. Homepage (we are after a basic website)
Hero Section:
A full-width image or video showcasing steel frames in construction or a finished project.
Tagline: Short, impactful tagline (e.g., "Strong Structures for Tomorrow").
Call-to-Action (CTA): A prominent "Get a Quote" or "Contact Us" button.
About Us (Snapshot Section):

A few lines about the company, emphasizing experience, certifications, and commitment to quality.
Include a "Learn More" button linking to the detailed About Us page.
Products/Services Section:

Feature the main products like steel frames for industrial, residential, and commercial projects.
Each category should have a "Learn More" link to a dedicated product page.
Project Showcase/Portfolio:

Display 2-3 featured projects with images, descriptions, and a "View All Projects" button.
Certifications & Partners:

Display logos of certifications (ISO, local building standards) and partnerships with construction companies or industry bodies.
Footer:

Contact information, quick links (Home, About, Products, Services, Contact), and social media icons.
2. Products Page
Overview:

A grid or list layout showing different steel frame products or services.
Each product should have a title, brief description, and a thumbnail image.
Individual Product Pages:

Detailed information on specific products (e.g., “Steel Frames for Residential Construction”):
Features: Highlight specific features like durability, eco-friendliness, precision, etc.
Technical Specs: Material grades, dimensions, finishes available.
Case Studies: A couple of client testimonials or case studies of where this product was used.
Downloadable Resources:

Technical datasheets or catalogs for users to download.
Include a form to capture user information before they download the document (optional for lead generation).
3. Projects/Portfolio Page
Gallery of Projects:
Display completed projects with high-quality images, each linked to a project detail page.
Filter options (e.g., industrial, residential, commercial).
Project Detail Pages:
A detailed description of the project, challenges, and how the steel frames were used.
other website we liked are:
https://www.brimwellframing.com.au/
https://quorvantframe.com.au/

1. Objective:
Create an informative, professional, and visually appealing website that promotes steel frame construction solutions, showcasing the company’s offerings, expertise, and projects.
The website should highlight the benefits of steel frames (e.g., durability, sustainability, and cost-efficiency) and cater to both B2B and B2C clients.
2. Target Audience:
Primary: Architects, builders, and construction companies.
Secondary: Homeowners, investors, and property developers looking for modern, durable construction solutions.

```html
<!DOCTYPE html>
<html lang="en">
<head>
<meta charset="utf-8">
<title>Brimwell – Steel Frame Construction</title>
<link href="https://fonts.googleapis.com/css2?family=Montserrat:wght@400;500;600;700;800&display=swap" rel="stylesheet">
<style>
:root{
  --blue:#1565c0;
  --blue-dark:#0d47a1;
  --ink:#111418;
  --ink-soft:#2a2d33;
  --grey:#ececec;
  --grey-mid:#d9d9d9;
  --text:#222;
  --muted:#666;
  --white:#fff;
  --client:#b9b9b9;
}
*{box-sizing:border-box;margin:0;padding:0}
html,body{width:1200px;height:3124px;overflow:hidden}
body{font-family:"Montserrat",Arial,sans-serif;color:var(--text);background:var(--white);position:relative}
.btn{display:inline-flex;align-items:center;justify-content:center;border-radius:30px;font-weight:700;font-size:13px;text-transform:uppercase;letter-spacing:.5px;white-space:nowrap}
.btn-blue{background:var(--blue);color:var(--white)}
.btn-outline{background:var(--white);color:var(--blue);border:2px solid var(--blue)}

/* header */
.site-header{height:104px;display:flex;align-items:center;padding:0 140px;justify-content:space-between}
.brand{font-weight:800;font-size:28px;letter-spacing:.5px;color:var(--ink);display:flex;align-items:center;gap:8px}
.brand-mark{width:14px;height:14px;background:var(--blue)}
.main-nav{display:flex;gap:26px;font-size:13px;font-weight:600;text-transform:uppercase;margin-left:60px}
.phone-btn{height:40px;padding:0 22px;gap:8px;font-size:14px}

/* hero */
.hero{position:absolute;top:104px;left:0;width:1200px;height:596px;background:linear-gradient(90deg,#0d3f8a 0%,#1565c0 38%,rgba(21,101,192,.55) 55%,#6f8da8 75%,#5d7a8e 100%)}
.hero-photo{position:absolute;inset:0 0 0 520px;background:linear-gradient(180deg,#8ea9c0,#50697c 70%,#3a4d5c)}
.hero-content{position:absolute;left:140px;top:100px;color:var(--white)}
.eyebrow{font-size:13px;font-weight:600;letter-spacing:.5px;text-transform:uppercase}
.hero h1{font-size:42px;line-height:1.12;font-weight:800;margin-top:14px;text-transform:uppercase}
.hero-tag{margin-top:22px;background:var(--white);color:var(--ink);font-weight:700;font-size:24px;width:300px;height:60px;border-radius:6px;display:flex;align-items:center;justify-content:center;white-space:nowrap}
.hero .btn{margin-top:30px;height:46px;padding:0 22px;background:var(--white);color:var(--blue)}
.hero-arrow{position:absolute;top:300px;width:20px;height:40px}

.category-cards{position:absolute;top:592px;left:140px;display:flex;gap:8px}
.category-card{width:300px;height:228px;border-radius:10px;padding:78px 26px 0;text-align:center;position:relative;font-size:13px;line-height:1.4}
.category-card h3{font-size:15px;font-weight:700;text-transform:uppercase;margin-bottom:10px}
.category-card .icon{position:absolute;top:-36px;left:50%;margin-left:-46px;width:92px;height:92px;border-radius:50%;background:var(--white);display:flex;align-items:center;justify-content:center;box-shadow:0 2px 6px rgba(0,0,0,.15)}
.category-card .btn{margin-top:16px;height:34px;padding:0 18px;font-size:11px}
.card-dark{background:var(--ink-soft);color:var(--white)}
.card-blue{background:var(--blue);color:var(--white)}
.card-light{background:var(--grey);color:var(--text)}
.card-dark .btn,.card-blue .btn{background:var(--white);color:var(--blue)}

/* about */
.about{position:absolute;top:880px;left:140px;width:920px;height:380px;display:flex;gap:40px}
.about-photo{width:400px;height:368px;border-radius:8px;background:linear-gradient(160deg,#c9cfd6,#8aa0b5 60%,#d78a3c)}
.about-text{padding-top:6px}
.about-text .eyebrow{color:var(--text)}
.about-text h2{font-size:44px;font-weight:800;text-transform:uppercase;margin:6px 0 20px;display:flex;gap:10px;align-items:center}
.tag-blue{background:var(--blue);color:var(--white);padding:2px 14px;border-radius:6px}
.about-text p{font-size:15px;line-height:1.55;color:var(--text);width:480px}
.about-text .btn{margin-top:30px;height:38px;padding:0 22px}

/* services */
.services{position:absolute;top:1300px;left:0;width:1200px;height:512px;background:var(--grey);text-align:center}
.services .eyebrow{margin-top:44px;display:block}
.section-title{font-size:44px;font-weight:800;text-transform:uppercase;display:flex;justify-content:center;gap:12px;margin-top:8px}
.service-grid{display:flex;gap:18px;justify-content:center;margin-top:40px}
.service{width:216px;height:266px;border-radius:4px;position:relative;overflow:hidden}
.service span{position:absolute;bottom:0;left:0;right:0;height:44px;background:var(--blue);color:var(--white);font-weight:700;font-size:14px;display:flex;align-items:center;justify-content:center;text-transform:uppercase}
.s1{background:linear-gradient(160deg,#7fa6c8,#4a6a8a)}
.s2{background:linear-gradient(160deg,#e9d3a6,#a4744a)}
.s3{background:linear-gradient(160deg,#b7b0a6,#6c625a)}
.s4{background:linear-gradient(160deg,#c7d4e0,#8a98a6)}

/* cta band */
.cta-band{position:absolute;top:1812px;left:0;width:1200px;height:122px;background:var(--ink);display:flex;align-items:center;padding:0 140px;gap:40px}
.cta-band .mark{width:56px;height:56px;background:var(--blue);flex:none}
.cta-band h2{color:var(--white);font-size:22px;font-weight:700;text-transform:uppercase;flex:1;white-space:nowrap}
.cta-band .btn{height:46px;width:270px;font-size:15px}

/* clients */
.clients{position:absolute;top:1976px;left:0;width:1200px;text-align:center}
.clients .eyebrow{display:block}
.client-row{display:flex;justify-content:center;gap:56px;margin-top:34px;color:var(--client);font-size:30px;font-weight:700;text-transform:uppercase;line-height:1}

/* enquiry */
.enquiry{position:absolute;top:2240px;left:140px;width:920px;height:540px}
.enquiry-photo{position:absolute;left:0;top:0;width:540px;height:540px;background:linear-gradient(180deg,#9fb3c6,#d6dde4 45%,#a66a2e)}
.enquiry-form{position:absolute;left:392px;top:68px;width:528px;height:444px;background:var(--blue);border-radius:6px;padding:22px 26px;color:var(--white)}
.enquiry-form .eyebrow{font-size:13px}
.enquiry-form h2{font-size:30px;font-weight:800;text-transform:uppercase;margin:2px 0 18px}
.field-row{display:flex;gap:14px;margin-bottom:16px}
.field{flex:1;height:38px;background:var(--white);color:var(--muted);font-size:12px;padding:11px 12px;border-radius:2px}
.field.tall{height:98px}
.enquiry-form .btn{margin-top:14px;height:36px;padding:0 20px;background:var(--white);color:var(--blue);font-size:11px}

/* footer */
.site-footer{position:absolute;top:2848px;left:0;width:1200px;height:276px;background:#000;color:var(--white)}
.footer-brand{position:absolute;left:140px;top:48px}
.footer-brand .brand{color:var(--white)}
.footer-brand p{font-size:14px;line-height:1.4;margin-top:18px;width:260px}
.footer-nav{position:absolute;right:140px;top:72px;display:flex;gap:18px;font-size:14px}
.socials{position:absolute;right:140px;top:120px;display:flex;gap:12px;align-items:center}
.social{width:30px;height:30px;border-radius:50%;border:2px solid var(--white)}
.socials .btn{height:40px;padding:0 22px;margin-left:14px;font-size:14px}
.footer-bottom{position:absolute;left:0;right:0;top:210px;border-top:1px solid #444;text-align:center;padding-top:20px;font-size:13px}
</style>
</head>
<body>

<header class="site-header">
  <div class="brand"><span class="brand-mark"></span>BRIMWELL</div>
  <nav class="main-nav"><span>Home</span><span>About us</span><span>Services</span><span>Products</span><span>Contact us</span></nav>
  <span class="btn btn-blue phone-btn">
    <svg width="14" height="14" viewBox="0 0 24 24" fill="#fff"><path d="M6.6 10.8a15 15 0 006.6 6.6l2.2-2.2a1 1 0 011-.25 11 11 0 003.6.6 1 1 0 011 1V20a1 1 0 01-1 1A17 17 0 013 4a1 1 0 011-1h3.5a1 1 0 011 1 11 11 0 00.6 3.6 1 1 0 01-.25 1z"/></svg>
    (02) 5550 1842</span>
</header>

<section class="hero">
  <div class="hero-photo" role="img" aria-label="Blue steel scaffolding and frames on a construction site"></div>
  <div class="hero-content">
    <span class="eyebrow">Welcome to Brimwell</span>
    <h1>Strong structures<br>for tomorrow</h1>
    <div class="hero-tag">Futuristic Technology</div>
    <span class="btn">Get a quote now</span>
  </div>
  <svg class="hero-arrow" style="left:30px" viewBox="0 0 20 40"><path d="M16 4L4 20l12 16" stroke="#fff" stroke-width="3" fill="none"/></svg>
  <svg class="hero-arrow" style="right:30px" viewBox="0 0 20 40"><path d="M4 4l12 16L4 36" stroke="#fff" stroke-width="3" fill="none"/></svg>
</section>

<div class="category-cards">
  <div class="category-card card-dark">
    <div class="icon"><svg width="44" height="44" viewBox="0 0 44 44" fill="none" stroke="#222" stroke-width="2.5"><path d="M6 22L22 8l16 14M11 18v18h22V18M18 36V26h8v10"/></svg></div>
    <h3>Residential</h3>
    <p>Lorem ipsum dolor sit amet, consectetur adipiscing elit, sed do eiusmod</p>
    <span class="btn">More info</span>
  </div>
  <div class="category-card card-blue">
    <div class="icon"><svg width="44" height="44" viewBox="0 0 44 44" fill="none" stroke="#222" stroke-width="2.5"><path d="M10 38V8h16v30M26 16h8v22M6 38h32M15 14h6M15 20h6M15 26h6M15 32h6"/></svg></div>
    <h3>Commercial</h3>
    <p>Lorem ipsum dolor sit amet, consectetur adipiscing elit, sed do eiusmod</p>
    <span class="btn">More info</span>
  </div>
  <div class="category-card card-light">
    <div class="icon"><svg width="44" height="44" viewBox="0 0 44 44" fill="none" stroke="#222" stroke-width="2.5"><path d="M6 38V20l9 6v-6l9 6v-6l9 6V8h5v30z"/></svg></div>
    <h3>Industrial</h3>
    <p>Lorem ipsum dolor sit amet, consectetur adipiscing elit, sed do eiusmod</p>
    <span class="btn btn-blue">More info</span>
  </div>
</div>

<section class="about">
  <div class="about-photo" role="img" aria-label="Construction worker in hard hat and safety vest at a building site"></div>
  <div class="about-text">
    <span class="eyebrow">Who we are</span>
    <h2>About <span class="tag-blue">Brimwell</span></h2>
    <p>Lorem ipsum dolor sit amet, consectetur adipiscing elit, sed do eiusmod tempor incididunt ut labore et dolore magna aliqua. Ut enim ad minim veniam, quis nostrud exercitation ullamco laboris nisi ut aliquip ex ea commodo consequat. Duis aute irure dolor in reprehenderit in voluptate velit esse cillum dolore eu fugiat nulla pariatur.</p>
    <span class="btn btn-outline">More info</span>
  </div>
</section>

<section class="services">
  <span class="eyebrow">What we do</span>
  <h2 class="section-title">Featured <span class="tag-blue">Services</span></h2>
  <div class="service-grid">
    <div class="service s1" role="img" aria-label="Steel wall frames under construction"><span>Wall frames</span></div>
    <div class="service s2" role="img" aria-label="Steel roof trusses"><span>Trusses</span></div>
    <div class="service s3" role="img" aria-label="Steel floor system joists"><span>Floor systems</span></div>
    <div class="service s4" role="img" aria-label="Structural steel framework"><span>Structural steel</span></div>
  </div>
</section>

<section class="cta-band">
  <span class="mark"></span>
  <h2>Do you need our excellent services?</h2>
  <span class="btn btn-blue">Contact us</span>
</section>

<section class="clients">
  <span class="eyebrow">Trusted partners</span>
  <h2 class="section-title">Our <span class="tag-blue">Clients</span></h2>
  <div class="client-row"><span>Tarvo</span><span>Kelmo</span><span>Ruvex</span><span>Olvana</span><span>pelio</span></div>
</section>

<section class="enquiry">
  <div class="enquiry-photo" role="img" aria-label="Engineers in hard hats reviewing building plans on site"></div>
  <div class="enquiry-form">
    <span class="eyebrow">Contact us</span>
    <h2>Send us enquiry</h2>
    <div class="field-row"><div class="field">First Name</div><div class="field">Last Name</div></div>
    <div class="field-row"><div class="field">Email Address</div><div class="field">Phone Number</div></div>
    <div class="field-row"><div class="field tall">Message</div></div>
    <span class="btn">Submit now</span>
  </div>
</section>

<footer class="site-footer">
  <div class="footer-brand">
    <div class="brand"><span class="brand-mark"></span>BRIMWELL</div>
    <p>Lorem ipsum dolor sit amet, consectetur adipiscing elit, sed do eiusmod</p>
  </div>
  <nav class="footer-nav"><span>Home</span><span>|</span><span>About Us</span><span>|</span><span>Services</span><span>|</span><span>Products</span><span>|</span><span>Contact Us</span></nav>
  <div class="socials">
    <span class="social"></span><span class="social"></span><span class="social"></span><span class="social"></span><span class="social"></span>
    <span class="btn btn-blue">(02) 5550 1842</span>
  </div>
  <div class="footer-bottom">Brimwell@2024. All Rights Reserved</div>
</footer>

</body>
</html>
```